Sprinkles & Tails 2nd Annual Fundraiser

I am a Realtor sponsoring the 2nd annual fundraiser on behalf of Allies of Harlow Vale Animal Haven. Like the flyer to be professional yet fun and inviting. Please see the attached file below. The 1st annual flyer was fun but not as professional, modern or inviting as I would have liked it to be.
Target Market(s)
Dog lovers in Ponte Vedra, Ponte Vedra Beach and Nocatee Florida
Logo Text
Needed
Font styles to use
Other font styles liked:
- Font that fits the style of the fundraiser
Colors
886aae
abd036
Requirements
Must have
- Please see the attached flyer and photos.
- This will be the 2nd Annual on Saturday, April 27, 2019 from 10AM - 1PM. Same location: Kendrick Realty, 418 Tillbrook Ave. Ponte Vedra FL 32075

```html
<!DOCTYPE html>
<html lang="en">
<head>
<meta charset="utf-8">
<title>Sprinkles &amp; Tails – 2nd Annual Flyer Variants</title>
<link href="https://fonts.googleapis.com/css2?family=Oswald:wght@400;500&family=Arimo:ital,wght@0,400;0,700;1,700&display=swap" rel="stylesheet">
<style>
  :root {
    --teal: #00a99d;
    --purple: #886aae;
    --green: #abd036;
    --white: #ffffff;
    --page: #ffffff;
    --photo-a: #d9dcd8;
    --photo-b: #eceae6;
    --frame-line: #cfcfcf;
  }
  * { box-sizing: border-box; margin: 0; padding: 0; }
  html, body { width: 1200px; height: 1200px; overflow: hidden; background: var(--page); }
  .canvas { position: relative; width: 1200px; height: 1200px; border: 1px solid var(--frame-line); }

  .flyer {
    position: absolute; width: 298px; height: 383px; background: var(--white);
    overflow: hidden; font-family: "Arimo", Arial, sans-serif;
  }
  .flyer--teal { --accent: var(--teal); --band: var(--teal); --ring: var(--teal); --footer: var(--teal); }
  .flyer--purple { --accent: var(--purple); --band: var(--green); --ring: var(--green); --footer: var(--green); }
  .pos-tl { left: 289px; top: 182px; }
  .pos-tr { left: 634px; top: 182px; }
  .pos-bl { left: 289px; top: 614px; }
  .pos-br { left: 634px; top: 614px; }

  .hero-photo {
    position: absolute; left: 0; top: 0; width: 100%; height: 166px;
    background: linear-gradient(180deg, var(--photo-b) 0%, var(--photo-a) 60%, var(--photo-b) 100%);
    opacity: .85;
  }
  .title { position: absolute; left: 0; width: 100%; text-align: center; color: var(--accent); }
  .title__year { top: 8px; font-family: "Oswald", sans-serif; font-weight: 500; font-size: 26px; line-height: 28px; letter-spacing: -.3px; transform: scaleX(.84); transform-origin: 148px 0; }
  .title__name { top: 34px; font-family: "Oswald", sans-serif; font-weight: 500; font-size: 19px; line-height: 20px; letter-spacing: -.3px; transform: scaleX(.82); transform-origin: 148px 0; }
  .title__tag { top: 54px; font-weight: 700; font-size: 6.5px; line-height: 8px; }

  .band { position: absolute; left: 0; top: 166px; width: 100%; height: 56px; background: var(--band); }
  .details {
    position: absolute; left: 47px; top: 155px; width: 204px; height: 79px; background: var(--accent);
    clip-path: polygon(9% 0, 91% 0, 100% 50%, 91% 100%, 9% 100%, 0 50%);
  }
  .details__row { position: absolute; left: 37px; font-family: "Oswald", sans-serif; font-size: 8.5px; line-height: 10px; color: var(--white); }
  .details__value { position: absolute; left: 52px; white-space: nowrap; }

  .photo-circle {
    position: absolute; border-radius: 50%; border: 5px solid var(--ring);
    box-shadow: 0 0 0 3px var(--white), 0 1px 4px 3px rgba(0,0,0,.15);
    background: radial-gradient(circle at 50% 40%, #b9b2a6, #6e6a62);
    z-index: 2;
  }
  .photo-circle--center { left: 104px; top: 64px; width: 92px; height: 92px; background: radial-gradient(circle at 50% 35%, #a8b7b1, #5c5e58); }
  .photo-circle--left { left: 54px; top: 82px; width: 74px; height: 74px; }
  .photo-circle--right { left: 174px; top: 93px; width: 66px; height: 66px; background: radial-gradient(circle at 50% 40%, #c49a6b, #6d6558); }

  .perks { position: absolute; top: 238px; list-style: none; color: var(--accent); font-weight: 700; font-size: 7.4px; line-height: 9.8px; }
  .perks li::before { content: "•"; margin-right: 5px; }
  .perks--left { left: 41px; }
  .perks--right { left: 166px; }

  .donate { position: absolute; left: 0; top: 271px; width: 100%; text-align: center; color: var(--accent); font-size: 6.2px; line-height: 8px; }
  .note { position: absolute; left: 0; top: 292px; width: 100%; text-align: center; color: var(--accent); font-size: 5.1px; line-height: 7px; }

  .footer { position: absolute; left: 0; top: 313px; width: 100%; height: 70px; background: var(--footer); color: var(--white); }
  .contact { position: absolute; top: 8px; width: 130px; text-align: center; font-size: 5.2px; line-height: 7px; }
  .contact--left { left: 6px; }
  .contact--right { left: 171px; }
  .contact__name { font-weight: 700; font-style: italic; }
  .contact__mark { margin-top: 5px; font-weight: 700; font-size: 6px; line-height: 7px; }
  .contact__mark::before { content: ""; display: inline-block; width: 5px; height: 5px; border-radius: 50%; background: var(--white); margin-right: 3px; vertical-align: middle; }
</style>
</head>
<body>
<main class="canvas">

  <article class="flyer flyer--teal pos-tl">
    <div class="hero-photo" role="img" aria-label="Faded photo of guests washing dogs at last year's event"></div>
    <h1 class="title title__year">2ND ANNUAL</h1>
    <h2 class="title title__name">SPRINKLES &amp; TAILS</h2>
    <p class="title title__tag">DOGGIE WASH EXTRAVAGANZA</p>
    <div class="band"></div>
    <div class="details">
      <p class="details__row" style="top:9px">DATE<span class="details__value">SATURDAY, APRIL 27, 2019</span></p>
      <p class="details__row" style="top:23px">TIME<span class="details__value">10AM - 1PM</span></p>
      <p class="details__row" style="top:37px">LOCATION<span class="details__value">KENDRICK REALTY CORP.</span></p>
      <p class="details__row" style="top:50px"><span class="details__value">LARKSPUR TOWN CENTER</span></p>
      <p class="details__row" style="top:63px"><span class="details__value">418 TILLBROOK AVENUE</span></p>
    </div>
    <div class="photo-circle photo-circle--left" role="img" aria-label="Photo of a schnauzer"></div>
    <div class="photo-circle photo-circle--center" role="img" aria-label="Photo of volunteers washing dogs"></div>
    <div class="photo-circle photo-circle--right" role="img" aria-label="Photo of a volunteer with a brown dog"></div>
    <ul class="perks perks--left"><li>FREE Doggie Wash</li><li>Food &amp; Beverages</li><li>Vendors (FREE give-a-ways)</li></ul>
    <ul class="perks perks--right"><li>Raffle Drawings</li><li>Grand Prize</li><li>Donations Welcome</li></ul>
    <p class="donate">To make a donation:&nbsp; https://www.pawpage.com/ahvah/<br>click:&nbsp; Donate</p>
    <p class="note">All domestic breeds from puppies to seniors invited.&nbsp; Please be<br>sure Furry Fido is tolerant of other dogs, crowds and bathing.</p>
    <footer class="footer">
      <div class="contact contact--left"><p class="contact__name">Marla Quinlan</p><p>Kendrick Realty Corp.</p><p>770.555.0142</p><p>marlaquinlan@kendrickrealtycorp.com</p><p class="contact__mark">Marla Quinlan</p></div>
      <div class="contact contact--right"><p class="contact__name">Denise Harrow</p><p>AHVAH</p><p>904.555.0187</p><p>denise-harrow@mailbox.net</p><p class="contact__mark">Harlow Vale Allies</p></div>
    </footer>
  </article>

  <article class="flyer flyer--purple pos-tr">
    <div class="hero-photo" role="img" aria-label="Faded photo of guests washing dogs at last year's event"></div>
    <h1 class="title title__year">2ND ANNUAL</h1>
    <h2 class="title title__name">SPRINKLES &amp; TAILS</h2>
    <p class="title title__tag">DOGGIE WASH EXTRAVAGANZA</p>
    <div class="band"></div>
    <div class="details">
      <p class="details__row" style="top:9px">DATE<span class="details__value">SATURDAY, APRIL 27, 2019</span></p>
      <p class="details__row" style="top:23px">TIME<span class="details__value">10AM - 1PM</span></p>
      <p class="details__row" style="top:37px">LOCATION<span class="details__value">KENDRICK REALTY CORP.</span></p>
      <p class="details__row" style="top:50px"><span class="details__value">LARKSPUR TOWN CENTER</span></p>
      <p class="details__row" style="top:63px"><span class="details__value">418 TILLBROOK AVENUE</span></p>
    </div>
    <div class="photo-circle photo-circle--left" role="img" aria-label="Photo of a schnauzer"></div>
    <div class="photo-circle photo-circle--center" role="img" aria-label="Photo of volunteers washing dogs"></div>
    <div class="photo-circle photo-circle--right" role="img" aria-label="Photo of a volunteer with a brown dog"></div>
    <ul class="perks perks--left"><li>FREE Doggie Wash</li><li>Food &amp; Beverages</li><li>Vendors (FREE give-a-ways)</li></ul>
    <ul class="perks perks--right"><li>Raffle Drawings</li><li>Grand Prize</li><li>Donations Welcome</li></ul>
    <p class="donate">To make a donation:&nbsp; https://www.pawpage.com/ahvah/<br>click:&nbsp; Donate</p>
    <p class="note">All domestic breeds from puppies to seniors invited.&nbsp; Please be<br>sure Furry Fido is tolerant of other dogs, crowds and bathing.</p>
    <footer class="footer">
      <div class="contact contact--left"><p class="contact__name">Marla Quinlan</p><p>Kendrick Realty Corp.</p><p>770.555.0142</p><p>marlaquinlan@kendrickrealtycorp.com</p><p class="contact__mark">Marla Quinlan</p></div>
      <div class="contact contact--right"><p class="contact__name">Denise Harrow</p><p>AHVAH</p><p>904.555.0187</p><p>denise-harrow@mailbox.net</p><p class="contact__mark">Harlow Vale Allies</p></div>
    </footer>
  </article>

  <article class="flyer flyer--teal pos-bl">
    <div class="hero-photo" role="img" aria-label="Faded photo of guests washing dogs at last year's event"></div>
    <h1 class="title title__year">2ND ANNUAL</h1>
    <h2 class="title title__name">SPRINKLES &amp; TAILS</h2>
    <p class="title title__tag">DOGGIE WASH EXTRAVAGANZA</p>
    <div class="band"></div>
    <div class="details">
      <p class="details__row" style="top:9px">DATE<span class="details__value">SATURDAY, APRIL 27, 2019</span></p>
      <p class="details__row" style="top:23px">TIME<span class="details__value">10AM - 1PM</span></p>
      <p class="details__row" style="top:37px">LOCATION<span class="details__value">KENDRICK REALTY CORP.</span></p>
      <p class="details__row" style="top:50px"><span class="details__value">LARKSPUR TOWN CENTER</span></p>
      <p class="details__row" style="top:63px"><span class="details__value">418 TILLBROOK AVENUE</span></p>
    </div>
    <div class="photo-circle photo-circle--left" role="img" aria-label="Photo of a schnauzer"></div>
    <div class="photo-circle photo-circle--center" role="img" aria-label="Photo of volunteers washing dogs"></div>
    <div class="photo-circle photo-circle--right" role="img" aria-label="Photo of a brown dog with a volunteer"></div>
    <ul class="perks perks--left"><li>FREE Doggie Wash</li><li>Food &amp; Beverages</li><li>Vendors (FREE give-a-ways)</li></ul>
    <ul class="perks perks--right"><li>Raffle Drawings</li><li>Grand Prize</li><li>Donations Welcome</li></ul>
    <p class="donate">To make a donation:&nbsp; https://www.pawpage.com/ahvah/<br>click:&nbsp; Donate</p>
    <p class="note">All domestic breeds from puppies to seniors invited.&nbsp; Please be<br>sure Furry Fido is tolerant of other dogs, crowds and bathing.</p>
    <footer class="footer">
      <div class="contact contact--left"><p class="contact__name">Marla Quinlan</p><p>Kendrick Realty Corp.</p><p>770.555.0142</p><p>marlaquinlan@kendrickrealtycorp.com</p><p class="contact__mark">Marla Quinlan</p></div>
      <div class="contact contact--right"><p class="contact__name">Denise Harrow</p><p>AHVAH</p><p>904.555.0187</p><p>denise-harrow@mailbox.net</p><p class="contact__mark">Harlow Vale Allies</p></div>
    </footer>
  </article>

  <article class="flyer flyer--purple pos-br">
    <div class="hero-photo" role="img" aria-label="Faded photo of guests washing dogs at last year's event"></div>
    <h1 class="title title__year">2ND ANNUAL</h1>
    <h2 class="title title__name">SPRINKLES &amp; TAILS</h2>
    <p class="title title__tag">DOGGIE WASH EXTRAVAGANZA</p>
    <div class="band"></div>
    <div class="details">
      <p class="details__row" style="top:9px">DATE<span class="details__value">SATURDAY, APRIL 27, 2019</span></p>
      <p class="details__row" style="top:23px">TIME<span class="details__value">10AM - 1PM</span></p>
      <p class="details__row" style="top:37px">LOCATION<span class="details__value">KENDRICK REALTY CORP.</span></p>
      <p class="details__row" style="top:50px"><span class="details__value">LARKSPUR TOWN CENTER</span></p>
      <p class="details__row" style="top:63px"><span class="details__value">418 TILLBROOK AVENUE</span></p>
    </div>
    <div class="photo-circle photo-circle--left" role="img" aria-label="Photo of a schnauzer"></div>
    <div class="photo-circle photo-circle--center" role="img" aria-label="Photo of volunteers washing dogs"></div>
    <div class="photo-circle photo-circle--right" role="img" aria-label="Photo of a brown dog with a volunteer"></div>
    <ul class="perks perks--left"><li>FREE Doggie Wash</li><li>Food &amp; Beverages</li><li>Vendors (FREE give-a-ways)</li></ul>
    <ul class="perks perks--right"><li>Raffle Drawings</li><li>Grand Prize</li><li>Donations Welcome</li></ul>
    <p class="donate">To make a donation:&nbsp; https://www.pawpage.com/ahvah/<br>click:&nbsp; Donate</p>
    <p class="note">All domestic breeds from puppies to seniors invited.&nbsp; Please be<br>sure Furry Fido is tolerant of other dogs, crowds and bathing.</p>
    <footer class="footer">
      <div class="contact contact--left"><p class="contact__name">Marla Quinlan</p><p>Kendrick Realty Corp.</p><p>770.555.0142</p><p>marlaquinlan@kendrickrealtycorp.com</p><p class="contact__mark">Marla Quinlan</p></div>
      <div class="contact contact--right"><p class="contact__name">Denise Harrow</p><p>AHVAH</p><p>904.555.0187</p><p>denise-harrow@mailbox.net</p><p class="contact__mark">Harlow Vale Allies</p></div>
    </footer>
  </article>

</main>
</body>
</html>
```